hello! I need a very simple modern business card for a new venture called The Quiet Harbour Asia. It's the very first Tech-Free retreat in Asia!

The concept is very unique. Basically a group of 12-15 people would go on a 3 to 4 days retreat where no phone or internet is allowed. The first retreat will take place in a beautiful villa in Bali by the sea. It will include yoga, meditation, art & writing workshops, swimming, hiking, cooking, healthy vegetarian meals, etc.

Reason: Thanks for your submissions. I still haven't found exactly what I'm after but the designs that haven't be eliminated are getting close.. Please keep in mind that it should be a simple, modern and upmarket business card. Thanks

Target Market(s)

Both men and women who would like to disconnect from life, computer and phone for 3/4 days. They can be either local or expats but based in Asia (Singapore, Hong Kong).
Client will have to pay for their own flight and then the price is around US$600 for a 3-day retreat including everything (accommodation, food, activities). It means clients already have a good income. They are usually working in marketing, advertising, digital media, public relations.

Industry/Entity Type

Internet

Font styles to use
Other font styles liked:
• anything modern you like

Colors
acd036
9bcb3c
f37022
f68d4d
1b1b1b
333333
acd037

Requirements
Must have
• Name: Rel Vontaine
Position: #screenwanderer
Company: The Quiet Harbour Asia (asia should be smaller than the rest)
- Email button - quietharbourasia@mailnest.example
- Facepage button - www.facepage.example/quietharbourasia
- Ticketloom button - www.quietharbourasia.ticketloom.example
Nice to have
• You can use my logo attached but it's something I designed quickly on Power Point so it would be nice to include your own version.
Should not have
• anything tacky or girly or childish. thanks

```html
<!DOCTYPE html>
<html lang="en">
<head>
<meta charset="utf-8">
<title>The Quiet Harbour Asia – Business Card</title>
<link rel="stylesheet" href="https://fonts.googleapis.com/css2?family=Coustard:wght@900&family=Cinzel:wght@400;600&family=Libre+Baskerville:wght@700&display=swap">
<style>
  :root {
    --lime: #acd036;
    --lime-deep: #7fa329;
    --leaf: #5f7f1c;
    --ink: #1b1b1b;
    --ink-soft: #222222;
    --ink-line: #333333;
    --chalk: #e2e2e2;
  }
  * { margin: 0; padding: 0; box-sizing: border-box; }
  html, body { width: 1050px; height: 1200px; overflow: hidden; background: var(--ink); }
  .canvas { position: relative; width: 1050px; height: 1200px; }
  .card { position: absolute; left: 0; width: 1050px; height: 600px; overflow: hidden; background: var(--ink); }
  .card--front { top: 0; }
  .card--back { top: 600px; border-top: 1px solid var(--ink-line); }
  .card svg.shapes { position: absolute; inset: 0; }

  .brand-mark { position: absolute; left: 67px; top: 50px; width: 126px; height: 126px; border-radius: 50%; background: var(--lime); }

  .company { position: absolute; right: 630px; top: 112px; text-align: right;
    font-family: "Coustard", Georgia, serif; font-weight: 900; color: var(--lime); }
  .company__line { display: block; font-size: 66px; line-height: 93px; }
  .company__region { display: block; font-size: 38px; line-height: 80px; }

  .person { position: absolute; right: 40px; top: 160px; text-align: right; color: var(--lime); font-family: "Cinzel", "Times New Roman", serif; }
  .person__name { font-size: 52px; font-weight: 600; letter-spacing: 2px; line-height: 60px; text-transform: uppercase; }
  .person__role { font-size: 20px; font-weight: 600; letter-spacing: 1px; text-transform: uppercase; }

  .contacts { position: absolute; left: 514px; top: 375px; list-style: none; }
  .contacts__item { display: flex; align-items: center; height: 48px; margin-bottom: 29px; }
  .contacts__icon { width: 48px; height: 48px; flex: none; }
  .contacts__text { margin-left: 18px; font-family: "Libre Baskerville", Georgia, serif; font-weight: 700; font-size: 19px; letter-spacing: -0.3px; color: var(--lime); white-space: nowrap; }
  .contacts__square { width: 46px; height: 46px; background: var(--lime-deep); }

  .band-title { position: absolute; left: 79px; top: 248px; font-family: "Coustard", Georgia, serif; font-weight: 900; color: var(--chalk); white-space: nowrap; }
  .band-title__main { font-size: 66px; }
  .band-title__region { font-size: 36px; margin-left: 46px; }
</style>
</head>
<body>
<main class="canvas">

  <section class="card card--front" aria-label="Card front">
    <svg class="shapes" width="1050" height="600" viewBox="0 0 1050 600" aria-hidden="true">
      <polygon points="540,146 1050,0 1050,600 540,600" fill="#1f1f1f"/>
      <polygon points="0,0 540,146 540,600 291,600 0,304" fill="#181818"/>
      <polygon points="410,0 670,0 540,146" fill="var(--leaf)"/>
      <polygon points="0,304 0,600 291,600" fill="var(--leaf)"/>
    </svg>

    <div class="brand-mark" role="img" aria-label="The Quiet Harbour Asia brand mark"></div>

    <h1 class="company">
      <span class="company__line">The</span>
      <span class="company__line">Quiet</span>
      <span class="company__line">Harbour</span>
      <span class="company__region">Asia</span>
    </h1>

    <div class="person">
      <p class="person__name">Rel Vontaine</p>
      <p class="person__role">#screenwanderer</p>
    </div>

    <ul class="contacts">
      <li class="contacts__item">
        <svg class="contacts__icon" viewBox="0 0 48 48" aria-hidden="true">
          <circle cx="24" cy="24" r="23" fill="var(--lime-deep)"/>
          <circle cx="24" cy="24" r="19" fill="#3d4a22"/>
          <rect x="12" y="16" width="24" height="16" rx="2" fill="#f2f2f2"/>
          <polyline points="12,17 24,26 36,17" fill="none" stroke="#8a8a8a" stroke-width="1.5"/>
        </svg>
        <span class="contacts__text">quietharbourasia@mailnest.example</span>
      </li>
      <li class="contacts__item">
        <span class="contacts__square" aria-hidden="true"></span>
        <span class="contacts__text">www.facepage.example/quietharbourasia</span>
      </li>
      <li class="contacts__item">
        <span class="contacts__square" aria-hidden="true"></span>
        <span class="contacts__text">www.quietharbourasia.ticketloom.example</span>
      </li>
    </ul>
  </section>

  <section class="card card--back" aria-label="Card back">
    <svg class="shapes" width="1050" height="600" viewBox="0 0 1050 600" aria-hidden="true">
      <polygon points="0,0 1050,0 525,250" fill="#202020"/>
      <polygon points="300,226 525,70 760,226" fill="#171717"/>
      <polygon points="0,373 1050,373 1050,600 0,600" fill="#151515"/>
      <rect x="0" y="226" width="1050" height="147" fill="var(--leaf)"/>
    </svg>
    <p class="band-title">
      <span class="band-title__main">The Quiet Harbour</span><span class="band-title__region">Asia</span>
    </p>
  </section>

</main>
</body>
</html>
```